Christmas Card Design

We are in need of a Christmas card design to send to other doctors this year. Uploaded files include our card from last year and our "VT" logo. Our goal is to incorporate our "VT" logo in whatever design we have. Last year, we used it as Christmas ornaments on a tree. The front of the card would also need to read "Happy Holidays". It could have a Santa, reindeer, snowman, or whatever ideas you have to give it the holiday feel.

```html
<!DOCTYPE html>
<html lang="en">
<head>
<meta charset="utf-8">
<title>Holiday Card – Inside Spread</title>
<link href="https://fonts.googleapis.com/css2?family=Lobster&family=Gentium+Plus&display=swap" rel="stylesheet">
<style>
  :root {
    --paper: #ffffff;
    --greeting: #1d9db3;
    --greeting-shadow: rgba(0, 0, 0, 0.3);
    --name-ink: #3f5f80;
    --signature-tone: #f0f2f4;
  }
  * { margin: 0; padding: 0; box-sizing: border-box; }
  html, body {
    width: 1200px; height: 927px; overflow: hidden;
    background: var(--paper);
  }
  .card-spread {
    position: relative; width: 1200px; height: 927px;
    background: var(--paper);
  }
  .greeting {
    position: absolute; left: 48px; top: 266px; width: 520px;
    text-align: center;
    font-family: "Lobster", "Brush Script MT", cursive;
    font-size: 56px; line-height: 72px;
    color: var(--greeting);
    text-shadow: 2px 3px 3px var(--greeting-shadow);
    letter-spacing: -1px;
    transform: rotate(-1deg);
  }
  .greeting-line { display: block; white-space: nowrap; }
  .signatory {
    position: absolute; width: 320px; text-align: center;
  }
  .signatory-name {
    font-family: "Gentium Plus", serif;
    font-size: 24px; line-height: 30px; color: var(--name-ink);
    letter-spacing: -0.6px; white-space: nowrap;
  }
  .signature-area {
    display: block; margin: 8px auto 0;
    width: 150px; height: 56px;
    background: var(--signature-tone);
    border-radius: 4px;
  }
  .col-left  { left: 584px; }
  .col-right { left: 888px; }
</style>
</head>
<body>
<main class="card-spread">
  <p class="greeting">
    <span class="greeting-line">May your days be bright,</span>
    <span class="greeting-line">and your heart be light!</span>
    <span class="greeting-line">Merry Christmas!</span>
    <span class="greeting-line">Happy Holidays!</span>
  </p>

  <section class="signatories">
    <div class="signatory col-left" style="top:27px"><p class="signatory-name">Marco L. Benton, M.D.</p><span class="signature-area" role="img" aria-label="Handwritten signature"></span></div>
    <div class="signatory col-right" style="top:27px"><p class="signatory-name">Henry A. Colbert, M.D.</p><span class="signature-area" role="img" aria-label="Handwritten signature"></span></div>

    <div class="signatory col-left" style="top:145px"><p class="signatory-name">Simon K. Adeyemi, M.D., F.A.C.P.</p><span class="signature-area" role="img" aria-label="Handwritten signature" style="margin-top:30px"></span></div>
    <div class="signatory col-right" style="top:145px"><p class="signatory-name">Peter J. Whitlow, M.D.</p><span class="signature-area" role="img" aria-label="Handwritten signature" style="margin-top:30px"></span></div>

    <div class="signatory col-left" style="top:297px"><p class="signatory-name">Walter G. Finch, M.D.</p><span class="signature-area" role="img" aria-label="Handwritten signature" style="margin-top:16px"></span></div>
    <div class="signatory col-right" style="top:297px"><p class="signatory-name">Brian T. Vo, M.D.</p><span class="signature-area" role="img" aria-label="Handwritten signature" style="margin-top:16px"></span></div>

    <div class="signatory col-left" style="top:441px"><p class="signatory-name">Daniel R. Ortega, M.D.</p><span class="signature-area" role="img" aria-label="Handwritten signature" style="margin-top:16px"></span></div>
    <div class="signatory col-right" style="top:441px"><p class="signatory-name">Arun Malhotra, M.D.</p><span class="signature-area" role="img" aria-label="Handwritten signature" style="margin-top:16px"></span></div>

    <div class="signatory col-left" style="top:575px"><p class="signatory-name">Nikhil Desai, M.D.</p><span class="signature-area" role="img" aria-label="Handwritten signature"></span></div>
    <div class="signatory col-right" style="top:575px"><p class="signatory-name">Eitan Korbel, M.D.</p><span class="signature-area" role="img" aria-label="Handwritten signature"></span></div>

    <div class="signatory" style="left:620px; top:697px"><p class="signatory-name">Ramon Esquivel, M.D.</p><span class="signature-area" role="img" aria-label="Handwritten signature" style="height:46px"></span></div>
    <div class="signatory" style="left:860px; top:697px"><p class="signatory-name">Wei Lin, M.D.</p><span class="signature-area" role="img" aria-label="Handwritten signature" style="height:46px"></span></div>

    <div class="signatory" style="left:718px; top:809px"><p class="signatory-name">Grace Tan M.D.</p><span class="signature-area" role="img" aria-label="Handwritten signature" style="height:60px"></span></div>
  </section>
</main>
</body>
</html>
```